Flicktor - photography in NYC - leveraging big data and robotics

We've got a photography business in NYC. It is kind of on-demand photographers, but actually is just five of us who work as a team. Over the last three years we've taken tens of thousands of photographs and are now sitting on a load of great work. We want to leverage that in a way that lets people book either by event type or location. So, they would click on Harrow Green and a load of examples of our work would pop up. Or Wedding Shower, and relevant examples would pop up. We've got the pictures structured pretty well to enable this. Now we just need a website that illustrates this and then leads through the booking process (time, location, date, contact etc.) and payment.

Target Market(s)

Everyone - corporates, real estate, tourists, families, headshots, bloggers, products, wedding showers, baby showers, engagements, venues, restaurants/bars, holiday pictures, Marlow Hall weddings, kids birthday parties, adult birthday parties, PR companies, corporate events.... long list.

Industry/Entity Type

Photographer

Number of Pages Required

5+ page

Colors

Designer to choose colors to be used in the design.

Requirements
Must have
• A great, engaging landing page which people can choose by event type or location. This would then pull in examples of our work in that location or in that event type. Then they go through the booking process. This is simple capturing key details - see here https://flicktorphoto.example/book/
Nice to have
• Social links
Should not have
• Nothing specific.

```html
<!DOCTYPE html>
<html lang="en">
<head>
<meta charset="utf-8">
<title>Flicktor – Photography in NYC</title>
<link rel="stylesheet" href="https://fonts.googleapis.com/css2?family=Saira+Semi+Condensed:wght@500;600;700&family=Saira:wght@500;600;700&display=swap">
<style>
  :root {
    --brand-red: #e8505a;
    --button-red: #e8696b;
    --white: #ffffff;
    --field-bg: rgba(236, 232, 232, 0.92);
    --field-text: #4a4444;
    --icon-grey: rgba(215, 212, 212, 0.85);
    --social: rgba(232, 80, 90, 0.9);
  }
  * { box-sizing: border-box; margin: 0; padding: 0; }
  html, body { width: 1200px; height: 598px; overflow: hidden; }
  body { font-family: "Saira", Arial, sans-serif; color: var(--white); }

  .landing { position: relative; width: 1200px; height: 598px; overflow: hidden; }

  .hero-photo {
    position: absolute; inset: 0;
    background:
      linear-gradient(90deg, rgba(0,0,0,0) 0%, rgba(0,0,0,0) 62%, rgba(20,22,28,0.55) 70%, rgba(44,70,110,0.85) 82%, rgba(52,80,122,0.95) 100%),
      linear-gradient(180deg, #dfe4e6 0%, #c9cccb 14%, #8a7f7a 30%, #6f625c 45%, #7c716d 60%, #a18f88 76%, #c7a8a0 88%, #d2cac6 100%);
  }

  .logo {
    position: absolute; left: 114px; top: 6px;
    font-family: "Saira", Arial, sans-serif; font-weight: 700;
    font-size: 70px; letter-spacing: 1px; color: var(--brand-red);
    text-transform: uppercase; line-height: 1;
  }

  .helpline { position: absolute; left: 889px; top: 26px; display: flex; gap: 8px; align-items: center; }
  .helpline-text { line-height: 1.05; }
  .helpline-label { font-size: 13.5px; font-weight: 600; color: var(--brand-red); }
  .helpline-number { font-size: 20px; font-weight: 600; letter-spacing: 0.5px; }

  .headline {
    position: absolute; left: 114px; top: 222px;
    font-family: "Saira Semi Condensed", Arial, sans-serif; font-weight: 600;
    font-size: 39px; line-height: 53px; letter-spacing: 0.3px;
  }
  .question-icon { position: absolute; left: 440px; top: 240px; }

  .event-form { position: absolute; left: 113px; top: 350px; display: flex; height: 44px; }
  .event-field {
    width: 321px; height: 44px; border: 0; padding: 0 8px;
    background: var(--field-bg); color: var(--field-text);
    font-family: Arial, Helvetica, sans-serif; font-size: 16px;
  }
  .event-field::placeholder { color: var(--field-text); }
  .next-button {
    width: 76px; height: 44px; border: 0;
    background: var(--button-red); color: var(--white);
    font-family: "Saira", Arial, sans-serif; font-size: 21px; font-weight: 500;
  }

  .copyright { position: absolute; left: 114px; top: 565px; font-size: 13px; font-weight: 600; }

  .social { position: absolute; left: 971px; top: 562px; display: flex; gap: 4px; list-style: none; }
  .social a { display: block; width: 26px; height: 26px; border-radius: 50%; background: var(--social); }
</style>
</head>
<body>
<main class="landing">
  <div class="hero-photo" role="img" aria-label="Blurred riverside street backdrop with a photographer in jeans holding a camera on the right"></div>

  <header>
    <div class="logo">Flicktor</div>
    <div class="helpline">
      <svg width="26" height="26" viewBox="0 0 26 26" aria-hidden="true">
        <circle cx="13" cy="13" r="11.5" fill="none" stroke="#fff" stroke-width="1.6"/>
        <path d="M9 7.5c-1 .6-1.6 1.6-1.3 3 .7 3 3.6 6.6 6.6 7.7 1.3.5 2.4.1 3.1-.8l-2-2.2-1.5.9c-1.3-.7-2.6-2.2-3.1-3.6l1.3-1.1z" fill="#fff"/>
      </svg>
      <div class="helpline-text">
        <div class="helpline-label">Need Help Call Us Today</div>
        <div class="helpline-number">555.014.2286</div>
      </div>
    </div>
  </header>

  <section>
    <h1 class="headline">What Do You<br>Want Pictures of</h1>
    <svg class="question-icon" width="78" height="76" viewBox="0 0 78 76" aria-hidden="true">
      <path d="M41 2a36 36 0 1 1-18 67L2 74l7-17A36 36 0 0 1 41 2z" fill="var(--icon-grey)"/>
      <text x="41" y="54" text-anchor="middle" font-family="Saira, Arial, sans-serif" font-weight="700" font-size="50" fill="#8d8787">?</text>
    </svg>
    <form class="event-form" action="https://flicktorphoto.example/book/">
      <input class="event-field" type="text" name="event" placeholder="Enter Your Event Name">
      <button class="next-button" type="submit">Next</button>
    </form>
  </section>

  <footer>
    <p class="copyright">Copyright © 2018 Flicktor. All Rights Reserved.</p>
    <ul class="social">
      <li><a href="#" aria-label="Social profile one"></a></li>
      <li><a href="#" aria-label="Social profile two"></a></li>
      <li><a href="#" aria-label="Social profile three"></a></li>
      <li><a href="#" aria-label="Social profile four"></a></li>
    </ul>
  </footer>
</main>
</body>
</html>
```